Summer Sunglass offer

Need a poster design for a spring / summer campaign. We are an opticians with good footfall. The design needs to be eye catching and aimed at 40 year old plus. The offer is Up to 50% off sunglass offer, t&c apply. (I have attached our last year campaign)
Also need a 2 sided A5 leaflet design (see attached)
I've uploaded a copy of our logo

A5 leaflet should read:

Grab a bargain on two great looks this summer Upto 50% off sunglasses
Look great and stay safe in the sun this summer

We want you to look great, feel fantastic and most of all stay safe in the sun this summer. That’s why we’re offering you 50% off prescription sunglasses with every complete pair of glasses you buy this summer or 25% off for prescription sunglasses with no other purchase.
Find you new summer looks from our gorgeous collection of frames in store. It matters to us that you look great in your new glasses as much as how well you see through them, so we’ll be on hand to help you find frames that suit you best.
What new looks will you go for? Smart or sassy? Formal or Fun? Whatever you’re in the mood for, you’ll find it in our collections this summer.
Call in today to find your new looks, and remember to bring your prescription if you don’t need an eye test.

Target Market(s)

40 + year old

Industry/Entity Type

Optician

Colors

Designer to choose colors to be used in the design.

Requirements
Must have
• Images, preferably a male and Female image

```html
<!DOCTYPE html>
<html lang="en">
<head>
<meta charset="utf-8">
<title>Summer Sunglasses Offer – Poster and Leaflet</title>
<link href="https://fonts.googleapis.com/css2?family=Bungee&family=Bungee+Shade&family=Poppins:ital,wght@0,400;0,600;1,400&family=Crimson+Text&display=swap" rel="stylesheet">
<style>
  :root {
    --backdrop: #4cbfc4;
    --paper: #f1f1f1;
    --navy: #2f5b8e;
    --teal: #3a9ea6;
    --teal-light: #6fc6c9;
    --white: #ffffff;
  }
  * { margin: 0; padding: 0; box-sizing: border-box; }
  html, body { width: 1200px; height: 828px; overflow: hidden; }
  body { background: var(--backdrop); position: relative; font-family: "Poppins", sans-serif; }

  .sheet { position: absolute; background: var(--paper); overflow: hidden; }
  .sheet--poster { left: 133px; top: 106px; width: 441px; height: 622px; }
  .sheet--leaflet { left: 625px; top: 106px; width: 438px; height: 620px; }

  .display { font-family: "Bungee", sans-serif; text-align: center; position: absolute; left: 0; right: 0; line-height: 1; }

  /* Poster */
  .poster__kicker { top: 36px; font-size: 22px; color: var(--teal); }
  .poster__title { top: 64px; font-size: 46px; color: var(--navy); }
  .poster__badge { position: absolute; left: 38px; top: 120px; width: 364px; height: 364px; }
  .poster__brand { position: absolute; top: 508px; left: 0; right: 0; display: flex; align-items: center; justify-content: center; gap: 12px; }
  .poster__brand-dot { width: 34px; height: 34px; border-radius: 50%; background: var(--teal); }
  .poster__brand-name { font-family: "Poppins", sans-serif; font-weight: 600; font-size: 22px; color: var(--navy); letter-spacing: 0.5px; line-height: 1.05; }
  .poster__url { top: 563px; font-size: 15px; color: var(--navy); }
  .poster__terms { position: absolute; left: 0; right: 0; bottom: 0; height: 28px; background: var(--navy); color: var(--white); font-family: "Crimson Text", serif; font-size: 8.2px; line-height: 10px; text-align: center; padding-top: 4px; }

  /* Leaflet */
  .leaflet__headline { position: absolute; left: 0; right: 0; font-weight: 600; color: var(--navy); text-align: center; font-size: 26px; line-height: 30px; }
  .leaflet__headline--top { top: 30px; }
  .leaflet__headline--mid { top: 378px; }
  .leaflet__offer { top: 108px; font-family: "Bungee Shade", sans-serif; font-size: 44px; color: var(--teal); }
  .leaflet__sub { top: 163px; font-size: 22px; color: var(--navy); }
  .leaflet__story { position: absolute; left: 20px; top: 209px; width: 400px; height: 144px; background: var(--navy); border-radius: 24px; color: var(--white); font-family: "Crimson Text", serif; font-size: 10px; line-height: 12.8px; text-align: center; padding: 14px 24px 0; }
  .leaflet__story p + p { margin-top: 10px; }
  .leaflet__moods { top: 455px; font-size: 33px; line-height: 37px; color: var(--teal); }
  .leaflet__note { position: absolute; left: 0; right: 0; top: 530px; text-align: center; font-style: italic; font-size: 16.5px; line-height: 20px; color: var(--navy); }
  .leaflet__footer { position: absolute; left: 0; right: 0; bottom: 0; height: 30px; background: var(--navy); color: var(--white); font-family: "Crimson Text", serif; font-size: 8.4px; line-height: 30px; text-align: center; }
</style>
</head>
<body>

<section class="sheet sheet--poster">
  <p class="display poster__kicker">Up to 50% off</p>
  <h1 class="display poster__title">Sunglasses</h1>

  <svg class="poster__badge" viewBox="0 0 364 364" aria-hidden="false">
    <defs>
      <radialGradient id="portraitTone" cx="50%" cy="45%" r="60%">
        <stop offset="0%" stop-color="#bfe6e6"/>
        <stop offset="60%" stop-color="#5fbcc0"/>
        <stop offset="100%" stop-color="#2f8e98"/>
      </radialGradient>
      <path id="badgeArc" d="M91.4 311.4 A158 158 0 1 1 272.6 311.4"/>
    </defs>
    <path class="badge-ring" d="M91.4 311.4 A158 158 0 1 1 272.6 311.4" fill="none" stroke="#2f5b8e" stroke-width="44"/>
    <circle cx="182" cy="182" r="136" fill="url(#portraitTone)" role="img" aria-label="Photo of a woman in round dark sunglasses and a white patterned jacket"/>
    <text font-family="Bungee, sans-serif" font-size="20" fill="#ffffff" dy="7">
      <textPath href="#badgeArc" startOffset="50%" text-anchor="middle">LOOK GREAT AND STAY SAFE IN THE SUN THIS SUMMER</textPath>
    </text>
  </svg>

  <div class="poster__brand">
    <span class="poster__brand-dot"></span>
    <span class="poster__brand-name">KELBRIDGE<br>EYECARE CENTRE</span>
  </div>
  <p class="display poster__url">www.kelbridgeeyecare.co.uk</p>

  <p class="poster__terms">Offer includes frame from selected range, standard single vision lenses, tint and UV protection.<br>Lens upgrades available at extra cost. Offer excludes Solvane frames, cannot be used with any other offer.</p>
</section>

<section class="sheet sheet--leaflet">
  <h2 class="leaflet__headline leaflet__headline--top">Grab a bargain on two<br>great looks this summer</h2>
  <p class="display leaflet__offer">Up to 50% off</p>
  <p class="display leaflet__sub">Sunglasses</p>

  <div class="leaflet__story">
    <p>We want you to look great, feel fantastic and most of all stay safe in the sun this summer. That’s why we’re offering you 50% off prescription sunglasses with every complete pair of glasses you buy this summer or 25% off for prescription sunglasses with no other purchase.</p>
    <p>Find you new summer looks from our gorgeous collection of frames in store. It matters to us that you love how you look in your new glasses as much as how well you see through them, so we’ll be on hand to help you find frames that suit you best.</p>
  </div>

  <h2 class="leaflet__headline leaflet__headline--mid">What new looks<br>will you go for?</h2>
  <p class="display leaflet__moods">Smart or sassy?<br>Formal or fun?</p>
  <p class="leaflet__note">Whatever you’re in the mood for, you’ll find it<br>in our collections this summer.</p>

  <p class="leaflet__footer">Call in today to find your new looks, and remember to bring your prescription if you don’t need an eye test.</p>
</section>

</body>
</html>
```